Postcard Design

I have an accounting firm and I would like to increase my customer base by a postcard mailout/letter dropI want a design that is eye catching and uses my logo. I specialise in small to medium business and offer services for commercial accounting and business advisory. I also want to offer a discount for new clients.Previously I had my website updated and would like to stay with the theme

Industry/Entity Type

Business Consultant

Font styles to use
Serif

Colors
b667aa
d3a5cc

Requirements
Must have
• the post card needs to be arty to attract attention. also business like

```html
<!DOCTYPE html>
<html lang="en">
<head>
<meta charset="utf-8">
<title>Corvell Accounting Services – Postcard</title>
<link href="https://fonts.googleapis.com/css2?family=Arimo:ital,wght@0,400;0,700;1,400;1,700&display=swap" rel="stylesheet">
<style>
  :root{
    --teal-dark:#2f9c99;
    --teal-light:#7fcfcb;
    --purple-deep:#8c3d82;
    --purple:#b667aa;
    --purple-soft:#d3a5cc;
    --white:#ffffff;
    --ink:#1d1d1d;
    --line:#9a9a9a;
  }
  *{box-sizing:border-box;margin:0;padding:0}
  html,body{width:849px;height:1200px;overflow:hidden}
  body{
    position:relative;
    font-family:"Arimo",Arial,sans-serif;
    background:linear-gradient(180deg,var(--teal-light) 0%,var(--teal-dark) 55%,var(--teal-light) 100%);
    color:var(--ink);
  }
  .card{position:absolute;left:62px;width:730px;background:var(--white);overflow:hidden}

  /* front side */
  .front{top:14px;height:596px}
  .front .photo{position:absolute;left:0;top:0;width:100%;height:340px;
    background:linear-gradient(120deg,#3b3a3f 0%,#8a7f78 35%,#d8cfc4 60%,#eef0ee 100%)}
  .front .logo-dot{position:absolute;right:40px;top:70px;width:62px;height:62px;border-radius:50%;background:var(--purple)}
  .name-band{position:absolute;left:0;top:342px;width:100%;height:70px;
    background:linear-gradient(90deg,var(--purple-deep),var(--purple));
    display:flex;align-items:center;padding-left:34px}
  .name-band h1{color:var(--white);font-weight:400;font-size:44px;letter-spacing:.3px}
  .tagline{position:absolute;left:0;width:100%;top:430px;text-align:center;
    font-style:italic;color:var(--purple-deep);font-size:31px}
  .services-short{position:absolute;left:0;width:100%;top:482px;text-align:center;font-size:22px;line-height:31px}
  .web-band{position:absolute;left:0;bottom:22px;width:100%;height:34px;background:var(--purple);
    color:var(--white);font-size:21px;text-align:center;line-height:34px}

  /* back side */
  .back{top:636px;height:558px}
  .back-head{position:absolute;left:18px;top:14px;width:480px}
  .back-head .brand{display:flex;align-items:center;gap:10px}
  .back-head .brand-dot{width:44px;height:44px;border-radius:50%;background:var(--purple);flex:none}
  .back-head h2{color:var(--purple-deep);font-weight:400;font-size:38px}
  .back-head .intro{margin:4px 0 0 58px;font-size:9.5px;line-height:12.5px;text-align:center}
  .stamp{position:absolute;right:52px;top:18px;width:90px;height:90px;border:1.5px solid #555}
  .ribbon{position:absolute;left:14px;top:152px;width:380px;height:70px}
  .address-lines{position:absolute;left:420px;top:222px;width:285px}
  .address-lines span{display:block;height:48px;border-bottom:1.5px solid var(--line)}
  .services-panel{position:absolute;left:18px;top:218px;width:362px;height:300px;
    background:linear-gradient(180deg,var(--purple) 0%,var(--purple-soft) 100%);padding:16px 18px 0}
  .services-panel h3{color:var(--white);font-size:28px;text-align:center;font-weight:700;margin-bottom:10px}
  .services-panel ul{list-style:none;color:var(--white);font-size:9px;line-height:11.2px}
  .services-panel li.group{font-weight:700;margin-top:6px}
  .contact{position:absolute;left:0;bottom:0;width:100%;height:74px;
    background:linear-gradient(90deg,var(--teal-dark),var(--teal-light));color:var(--white);padding:6px 0 0 60px}
  .contact h4{font-size:19px;font-weight:700;margin-bottom:2px}
  .contact p{font-size:11px;line-height:13px}
  .contact .row{display:flex;align-items:center;gap:5px}
</style>
</head>
<body>

<section class="card front">
  <div class="photo" role="img" aria-label="Photo of three colleagues in a business meeting at an office desk"></div>
  <div class="logo-dot"></div>
  <div class="name-band"><h1>Corvell Accounting Services</h1></div>
  <p class="tagline">Accountants with professional integrity</p>
  <p class="services-short">Commercial Accounting Services<br>Business Advisory – Compliance</p>
  <div class="web-band">www.corvellaccounting.com.au</div>
</section>

<section class="card back">
  <header class="back-head">
    <div class="brand"><span class="brand-dot"></span><h2>Corvell Accounting Services</h2></div>
    <p class="intro">Corvell Accounting Services uses cloud practice software for the highest efficiency<br>
      when working with our clients in the Hunter region, Australia.<br>
      All services are provided with an engagement letter and quote –<br>
      for your reference and protection</p>
  </header>
  <div class="stamp"></div>

  <div class="address-lines"><span></span><span></span><span></span><span></span><span></span></div>

  <div class="services-panel">
    <h3>OUR SERVICES</h3>
    <ul>
      <li>Accounting Packages and Training</li>
      <li>Bookkeeping including GST, BAS preparation and PAYG</li>
      <li>Budget Preparation, Cash Flow and Forecasting</li>
      <li>Business Activity Statement Preparation</li>
      <li>Payroll Setup and Management</li>
      <li>Debt and Accounts Receivable Management</li>
      <li>Financial Statement Preparation</li>
      <li>Income Tax Returns</li>
      <li>Individual Tax Returns and Planning</li>
      <li>Structuring and Planning for Growth</li>
      <li class="group">Business and Advisory Services</li>
      <li>Business Structure Reviews</li>
      <li>Cash Flow Management and Reporting</li>
      <li>Key Performance Indicators</li>
      <li>Management Reports</li>
      <li>Succession and Exit Planning</li>
      <li>Self Managed Superannuation Funds</li>
      <li>Tax Compliance – Registered Agent</li>
    </ul>
  </div>

  <svg class="ribbon" viewBox="0 0 380 70" aria-label="Boost Your Business' Profits">
    <polygon points="0,12 380,0 352,32 380,62 0,70" fill="#8c3d82"/>
    <text x="18" y="46" fill="#ffffff" font-family="Arimo, Arial, sans-serif" font-style="italic" font-weight="700" font-size="25">Boost Your Business' Profits</text>
  </svg>

  <footer class="contact">
    <h4>CONTACT US</h4>
    <p>Corvell Accounting Services</p>
    <p>Level 3, Suite 302 - 28 Harlow Street - Newcastle, Australia 2300</p>
    <p class="row">
      <svg width="10" height="10" viewBox="0 0 10 10"><path d="M2 1l2 2-1 1.2a6 6 0 0 0 2.8 2.8L7 6l2 2-1.2 1.5C4 9 1 6 .5 2.2z" fill="#fff"/></svg>
      +61 2 4900 1234
      &nbsp;
      <svg width="11" height="9" viewBox="0 0 11 9"><rect x=".5" y=".5" width="10" height="8" fill="none" stroke="#fff"/><path d="M.5.5l5 4 5-4" fill="none" stroke="#fff"/></svg>
      hello@corvellaccounting.com.au
    </p>
  </footer>
</section>

</body>
</html>
```